Rovi is a not-for-profit college planning organization serving the students of Louisiana's public and private schools. This contest is one of many scholarship opportunities that we will offer to the Senior High School Class of 2014. This flyer design will be distributed to all high school seniors, encouraging them to submit a drawing, painting or graphic design using the theme "Louisiana Holiday Cheer and Happy New Year". The winning student design will be used on our organization's Holiday Greeting Card and will be mailed in December of 2012 to all of our clients.
This design will be printed as an 8-1/2" x 11" flyer.
A copy of last year's winning flyer is attached for your use in creating a 2013 Winter Sketch Challenge Flyer. The deadline will be November 1, 2013.
This flyer will be distributed to Louisiana high school seniors which will range from 17-18 years old.

```html
<!DOCTYPE html>
<html lang="en">
<head>
<meta charset="utf-8">
<title>Rovi's 2013 Winter Sketch Challenge</title>
<link rel="stylesheet" href="https://fonts.googleapis.com/css2?family=Monoton&family=Didact+Gothic&family=Oswald:wght@500;600&display=swap">
<style>
  :root {
    --page: #ffffff;
    --flyer-deep: #12303f;
    --flyer-mid: #1f4c63;
    --flyer-light: #6fa3bb;
    --panel: #163646;
    --panel-edge: #d96b6b;
    --cream: #f1e7b6;
    --ice: #bfe6f2;
    --blush: #ffd2cc;
    --coral: #ff6f6f;
    --navy-text: #15303d;
    --band: rgba(205, 228, 238, 0.55);
  }
  * { margin: 0; padding: 0; box-sizing: border-box; }
  html, body { width: 1200px; height: 1000px; overflow: hidden; background: var(--page); }
  .flyer {
    position: absolute; left: 222px; top: 25px; width: 741px; height: 960px;
    background: linear-gradient(170deg, var(--flyer-deep) 0%, var(--flyer-mid) 45%, #5d8ea5 75%, var(--flyer-mid) 100%);
    box-shadow: 0 4px 14px rgba(0,0,0,0.45);
    overflow: hidden;
  }
  .decor-circles {
    position: absolute; left: 0; top: 0; width: 120px; height: 700px;
    background: linear-gradient(180deg, rgba(120,190,215,0.35), rgba(60,120,150,0.15));
  }
  .decor-splash {
    position: absolute; left: 0; top: 380px; width: 480px; height: 320px;
    background: radial-gradient(ellipse at 30% 40%, rgba(215,245,255,0.85), rgba(120,180,205,0.35) 55%, rgba(31,76,99,0) 80%);
  }
  .panel {
    position: absolute; background: var(--panel);
    border: 1.5px solid var(--panel-edge);
    box-shadow: 0 6px 12px rgba(0,0,0,0.5);
    transform: rotate(-8deg);
  }
  .title-panel { left: 92px; top: 70px; width: 630px; height: 250px; padding: 14px 26px 0 0; text-align: right; }
  .title {
    font-family: "Monoton", sans-serif; color: var(--cream);
    font-size: 47px; line-height: 58px; font-weight: 400; white-space: nowrap;
  }
  .tagline {
    font-family: "Didact Gothic", sans-serif; color: var(--ice);
    font-size: 33px; line-height: 38px; margin-top: 8px; padding-right: 6px;
  }
  .theme-label {
    position: absolute; left: 86px; top: 415px; width: 205px; height: 44px;
    background: var(--panel); border: 1.5px solid var(--ice);
    transform: rotate(-8deg);
    font-family: "Didact Gothic", sans-serif; color: #ffffff; font-size: 25px;
    line-height: 40px; text-align: center; z-index: 2;
  }
  .theme-label em { font-size: 20px; }
  .theme-panel { left: 215px; top: 395px; width: 500px; height: 160px; padding: 20px 22px 0 0; text-align: right; }
  .theme {
    font-family: "Oswald", sans-serif; font-weight: 600; color: var(--blush);
    font-size: 40px; line-height: 52px; white-space: nowrap;
  }
  .media-panel { left: 466px; top: 565px; width: 262px; height: 110px; padding: 8px 12px; }
  .media {
    font-family: "Didact Gothic", sans-serif; color: var(--ice); font-size: 16.5px; line-height: 20px;
  }
  .deadline-panel { left: 510px; top: 683px; width: 175px; height: 100px; padding: 8px 12px; background: var(--flyer-mid); }
  .deadline {
    font-family: "Didact Gothic", sans-serif; color: var(--coral); font-size: 22px; line-height: 26px;
  }
  .award-band {
    position: absolute; left: 0; top: 690px; width: 741px; height: 190px; background: var(--band);
  }
  .award-headline {
    position: absolute; left: 20px; top: 705px;
    font-family: "Oswald", sans-serif; font-weight: 600; font-size: 41px; color: var(--navy-text);
  }
  .award-headline .amount { color: var(--coral); }
  .award-sub {
    position: absolute; left: 22px; top: 765px;
    font-family: "Oswald", sans-serif; font-weight: 500; font-size: 22px; color: #23495c;
  }
  .award-rule { position: absolute; left: 0; top: 807px; width: 524px; height: 2px; background: var(--navy-text); }
  .contact {
    position: absolute; left: 22px; top: 815px; display: flex; gap: 26px;
    font-family: "Oswald", sans-serif; font-weight: 500; font-size: 30px; color: var(--navy-text);
  }
  .footer {
    position: absolute; left: 0; top: 895px; width: 741px; height: 34px;
    background: linear-gradient(90deg, #102a37, #1b4256);
    font-family: "Didact Gothic", sans-serif; color: #ffffff; font-size: 11.5px;
    line-height: 34px; padding-left: 22px; white-space: nowrap;
  }
  .footer strong { font-family: "Oswald", sans-serif; font-weight: 500; font-size: 15px; }
</style>
</head>
<body>
  <main class="flyer">
    <div class="decor-circles" role="img" aria-label="Decorative concentric circle pattern"></div>
    <div class="decor-splash" role="img" aria-label="Decorative paint splatter"></div>

    <section class="panel title-panel">
      <h1 class="title">ROVI'S 2013 WINTER<br>SKETCH CHALLENGE</h1>
      <p class="tagline">Your art could be featured<br>in Rovi's 2013 Holiday<br>Greeting Card</p>
    </section>

    <div class="theme-label">The theme <em>is</em></div>
    <section class="panel theme-panel">
      <p class="theme">Louisiana Holiday Cheer<br>and Happy New Year</p>
    </section>

    <section class="panel media-panel">
      <p class="media">Original Photography, Pen<br>Pencil,Water Color,Crayon<br>Charcoal and<br>More Accepted..</p>
    </section>

    <div class="award-band"></div>

    <section class="panel deadline-panel">
      <p class="deadline">DEADLINE<br>November 1<sup>st</sup><br>2013</p>
    </section>

    <p class="award-headline">Up to <span class="amount">6000$</span> in Scholarships</p>
    <p class="award-sub">Awarded to Lousiana High School Seniors</p>
    <div class="award-rule"></div>
    <p class="contact"><span>www.askRovi.org</span><span>800-555-0147</span></p>

    <footer class="footer">Lousiana's Non-Profit resource for College Planning. For Details and Guidelines visit our website at <strong>www.askRovi.org</strong></footer>
  </main>
</body>
</html>
```